Letterhead for a German Distribution/Manufacturing Company

We need a professional Letterhead in a unique Design.
not to playful.
The Letterhead has to show show that we are a international company with headquater in Germany.
all details like adress, Vat Tax Number, Bank Accout, Eori, email, Company number has to be on the Letterhead.
for example use: VAT TAX DE5704168 Bank Account: Norrfeld Bank IBAN DE421705238ß310482 Swift: KOLV3154802 EORI 3041296587 Company Number: HRB 61508 Adress: VOLTRINA UG Amsel Strasse 7 Postal Code 04683 City Velmstadt Country: Germany Email: info@voltrina-example.com
the design can be colored but doesnt have to be
Industry/Entity Type
Manufacturing and international distribution
Requirements
Must have
- show that we are a international company with headquater in Germany. our company infos and logo

```html
<!DOCTYPE html>
<html lang="en">
<head>
<meta charset="utf-8">
<title>VOLTRINA Letterhead</title>
<link href="https://fonts.googleapis.com/css2?family=Montserrat:wght@400;500&display=swap" rel="stylesheet">
<style>
  :root {
    --backdrop: #e9e9ea;
    --paper: #ffffff;
    --ink: #1d1d1d;
    --band: #1f1f1f;
    --band-text: #f4f4f4;
    --sign: #d6d6d6;
  }
  html, body {
    margin: 0;
    width: 1200px;
    height: 874px;
    overflow: hidden;
    background: var(--backdrop);
    font-family: "Montserrat", Arial, sans-serif;
    color: var(--ink);
  }
  .letterhead {
    position: absolute;
    left: 310px;
    top: 24px;
    width: 580px;
    height: 826px;
    background: var(--paper);
    box-shadow: 0 4px 18px rgba(0,0,0,0.12);
    overflow: hidden;
  }
  .brand {
    position: absolute;
    left: 52px;
    top: 62px;
    display: flex;
    align-items: center;
    gap: 12px;
  }
  .brand-dot {
    width: 34px;
    height: 34px;
    border-radius: 50%;
    background: var(--ink);
  }
  .brand-name {
    font-size: 30px;
    font-weight: 400;
    letter-spacing: 1px;
  }
  .sender {
    position: absolute;
    right: 52px;
    top: 58px;
    font-size: 8.5px;
    line-height: 12px;
    font-style: normal;
  }
  .sender .email { display: flex; align-items: center; gap: 4px; }
  .recipient {
    position: absolute;
    left: 52px;
    top: 150px;
    font-size: 10.5px;
    line-height: 14px;
  }
  .body-copy {
    position: absolute;
    left: 90px;
    top: 230px;
    width: 440px;
    font-size: 10.5px;
    line-height: 14.5px;
  }
  .body-copy p { margin: 0 0 20px; }
  .closing { margin-top: 4px; }
  .signature {
    width: 140px;
    height: 48px;
    margin-top: 10px;
    background: linear-gradient(90deg, var(--sign), #f2f2f2);
    border-radius: 3px;
  }
  .legal-band {
    position: absolute;
    left: 0;
    right: 0;
    bottom: 0;
    height: 170px;
    background: var(--band);
    color: var(--band-text);
    box-sizing: border-box;
    padding: 70px 0 0 250px;
    font-size: 10px;
    line-height: 15px;
    white-space: nowrap;
  }
</style>
</head>
<body>
  <main class="letterhead">
    <header class="brand">
      <span class="brand-dot"></span>
      <span class="brand-name">VOLTRINA</span>
    </header>

    <address class="sender">
      VOLTRINA UG Amsel Strasse 7<br>
      Postal Code 04683 City Velmstadt<br>
      Country: Germany<br>
      <span class="email">
        <svg width="9" height="7" viewBox="0 0 9 7" aria-hidden="true"><rect x="0.5" y="0.5" width="8" height="6" fill="none" stroke="#1d1d1d"/><path d="M0.5 0.5 L4.5 4 L8.5 0.5" fill="none" stroke="#1d1d1d"/></svg>
        info@voltrina-example.com
      </span>
    </address>

    <section class="recipient">
      Mr/s<br>
      First Name and Last Name<br>
      Company Name<br>
      Address
    </section>

    <section class="body-copy">
      <p>Lorem Ipsum is simply dummy text of the printing and typesetting industry. Lorem Ipsum has been the industry's standard dummy text ever since the 1500s, when an unknown printer took a galley of type and scrambled it to make a type specimen book. It has survived not only five centuries, but also the leap into electronic typesetting, remaining essentially unchanged. It was popularised in the 1960s with the release of Fontrex sheets containing Lorem Ipsum passages.</p>
      <p>he standard chunk of Lorem Ipsum used since the 1500s is reproduced below for those interested. Sections 1.10.32 and 1.10.33 from "de Finibus Bonorum et Malorum" by Varonius are also reproduced in their exact original form, accompanied by English versions from the 1914 translation by H. Ellwood. Lorem ipsum dolor sit amet, consectetur adipiscing elit, sed do eiusmod tempor incididunt ut labore et dolore magna aliqua.</p>
      <p>It is a long established fact that a reader will be distracted by the readable content of a page when looking at its layout. The point of using Lorem Ipsum is that it has a more-or-less normal distribution of letters, as opposed to using 'Content here, content here', making it look like readable English. Many desktop publishing packages and web page editors now .</p>
      <div class="closing">Your Sincerely,</div>
      <div class="signature" role="img" aria-label="Handwritten signature"></div>
    </section>

    <footer class="legal-band">
      VAT TAX DE5704168 &nbsp;|&nbsp; Company Number: HRB 61508<br>
      Bank Account: Norrfeld Bank IBAN DE421705238ß310482<br>
      Swift: KOLV3154802 EORI 3041296587
    </footer>
  </main>
</body>
</html>
```